webpage design for www.brightpathYOU.com

Hi-
I am creating a website about weight loss through healthy eating. The target audience is 80% women, of all races and ethnic backgrounds, in the 35-55 age range, all of whom are overweight and want to lose weight.
At first (which is where you come in), the website will be strictly informational, and products for sale will be added later.
Obviously not all of the following information can be incorporated into the design, but to give you some background, here is what I am doing.
First thing the site visitor needs to know is what the website is about. It’s about them, and how they can lose weight effectively. It’s only secondarily about me, and the w
ebsite must talk about me only from the point of view of how can I help them. It is your job to create a webpage where I can do just that. I have the content of this page ready to go, but I need you to create a beautiful, enticing, and effective framework to put it all in. You do not need to enter any copy except for the small amount noted below.
My clients are looking for a weight loss method or program that is effective, healthy, and long-lasting. This system addresses those needs. It's important for the clients to know that with the brightpathYOU system, there is no hunger, no deprivation, no pills, no weighing foods or calorie counting, no special products to buy, among other things.
And not only does the weight come off, but there are other health benefits as well. The brightpathYOU system can lower cholesterol, blood pressure, dependence on insulin for type 2 diabetics, reduce risk of heart disease and certain types of cancer, among other things-and this has been medically documented.
When I say "healthy eating", the focus of this program is on vegetables, fruits, and grains, with no added fat, but I do not want the main page to highlight that, since the whole notion of lots of veggies can scare people away. Pictures of fruits and veggies are fine. I'll introduce scary words like “vegan” and “no added fat” into the written materials and in the video, but there is no point in chasing people away too quickly!
The banner headline should have incorporated into it, in addition to the business name, the following: "Lose weight...improve your looks...improve your health...transform your life". You will need to choose a typeface and add this copy.
I would like to have a collage of healthy, happy, slender people of all ages (mostly women), in group and social settings-but not all exercising or doing yoga or jogging, since many of my target audience are couch potatoes (at least right now). If you do use any pictures of overweight people, they should be solitary, not part of a group, and definitely not looking happy!. I was thinking of having this only in the banner at top, but if you find a way to make the site attractive by adding a thin border with this as well, feel free.
Or, since I am not a design person by any stretch of the imagination, if you have another idea as to the banner design and the rest, I am certainly open to it.
In addition to the banner headline, I want a two-column design on the lower section, one being a narrower sidebar on the right, with a place for the customer to enter his/her name, and the following: Free video & eBook" "Every Plate Tells A Story, Every Meal Builds A Habit-And How You Can Shape Yours Today", and they get this in exchange for entering their first and last name, and email address. I can link this to AWeber later. I have a video widget, as well as a bunch more, in place, so you do not need to create or order those.
I will later add something to this section about no spam will be sent.
Below that in the same thinner column on the right should be an archives section, which you will need to create if the Wordpress theme doesn't have it already. This should be the same on all pages, except the single column pages, and since they will have sales pitches, should not have anything else.
The wider, main column I want to have three particular areas: One, is video. Two is text. Three is comments.
I will be using a LOT of video, but below each video I want to be able to place the text for the video (not everyone wants to watch a video), I want a static first page, but no comments section on the first page (I may want to add a comments section later, but not now).
The next page will be a basic "about me" page. This will be a video with text below in the main section, and will have the same enter your email info on the right side bar. No need to have "comments" below this. I've uploaded a picture of me, which should appear on this page, as well as on the main page.
Then will be a blog page, again the same layout: videos, which I can add to consecutively, with "comments" below, (which I can approve or disapprove before they get posted), with the offer in the right sidebar. Any videos will also show up in the archives section.
And a "recipes" page, video and text, plus comments section, with the email offer in the sidebar. These will show up as an archives section as well. I’ll add recipes and cooking videos later.
Then will be a "Products" page, which will for now be blank (I haven't created them yet), but with the email offer in the right side bar. No comments section to this one.
And a Contact Us page, no comments section either. I'll add the contact information later.
Across bottom of each page, perhaps in a somewhat contrasting color, will be a disclaimer, which I’ll need to be able to edit. This will be in small print, and should say something like, “This website expresses the opinions of the author, is intended for informational and educational purposes only, should not be construed as medical or dietary advice, and is not intended to be a substitute for same. Before changing diets, medications, or before undertaking a weight loss regimen, be sure to consult with your physician. This information is not intended to diagnose or treat any illness or health problems you may be experiencing, so kindly address your doctor with these concerns.” You can copy and paste this text.
Each page should also say “copyright 2014, Ned Brook”, which you will need to add.
Beyond that I will need single blank column pages which I will later make into landing, thank you, and so on pages. This will not be visible from the main page, though.

This will be done in Wordpress. I have the URL and the page is set up on Wordpress already, but I will need you to integrate the design into my Wordpress site when it is completed, so you will need a working knowledge of Wordpress. So the final winner will need to have the capability of coding the design and uploading it into my website and server. When you are done, it will be a complete and turnkey website, and all I have to do is add the copy and videos.

I am not particular as to a Wordpress theme, as long as it's an unpaid one, but if you find a paid one that you think is useable and needs to be paid for, let me know so I can check it out.
And I will need to be easily able to change and edit anything in the webpage on Wordpress at the end, after you are finished, with NO HTML, so any theme must be dummy friendly (I am the dummy, by the way!). (I have a basic familiarity with Wordpress, but none of HTML.)

Hopefully this gives you more than enough information to work with. Even though this page is a bit complicated, the actual website should be pretty simple looking, not busy or full of distractions, with only a few focal points.
Updates

Hi-information has been updated, I've changed my status to "committed", and I've uploaded a lot of pictures of fruit and veggies for you to use.  Thanks for your attention!
Ned

Target Market(s)

As stated above, "The target audience is 80% women, of all races and ethnic backgrounds, in the 35-55 age range, all of whom are overweight and want to lose weight."

Industry/Entity Type

Cooking

Font styles to use
Serif

Requirements
Must have
• The home page serves two purposes: one, to introduce the reader to the material, but two, and equally important, to build my email list. To that end, the opt in form on the right should say prominently, Free video & eBook" "Every Plate Tells A Story, Every Meal Builds A Habit-And How You Can Shape Yours Today", and below that should be the opt in boxes.
The banner can be scrolling, to attract ATTENTION, should lead to the ACTION of watching the video, which will have in it a CALL TO ACTION of signing up for the hopefully compelling OFFER of the free ebook and video-and of course the newsletter. My purpose on page one is to directly address the question of "What's in it for me?", and then to deliver with the video and ebook offer.
I've uploaded a bunch of pictures of veggies and fruit-feel free to use them, as they are all mine.
Possibly a scrolling banner could be used with alternating pictures of happy, slender people alternating with pictures, and the captions of "lLose weight...improve your looks...improve your health...transform your life"

Emphasis should be on healthy eating, not on pounds lost or measuring one's waist or some such thing.

Banner headline should include: ""Lose weight...improve your looks...improve your health...transform your life"
Should not have
• Please avoid pictures of picture-perfect people, scales, and so on-I do not want this to be some generic, cookie-cutter weight loss web site. This is about weight loss from a different point of view-and I don't think this will come across in the webpage, but the concept will be introduced later. It's about weight loss as a byproduct of changing eating habits from unhealthy to healthy.

```html
<!DOCTYPE html>
<html lang="en">
<head>
<meta charset="utf-8">
<title>brightpathYOU – Healthy Eating Blog</title>
<link rel="stylesheet" href="https://fonts.googleapis.com/css2?family=Arvo:wght@400;700&family=Open+Sans:ital,wght@0,400;0,600;0,700;1,400&display=swap">
<style>
:root{
  --brand-blue:#0d8ccc;
  --brand-blue-dark:#0a7cb6;
  --ink:#111111;
  --text:#3a3a3a;
  --muted:#8a8a8a;
  --panel-dark:#1f1f1f;
  --field-bg:#f4f4f4;
  --line:#d9d9d9;
  --hero-bg:#e6e7e8;
  --white:#ffffff;
}
*{box-sizing:border-box;margin:0;padding:0}
html,body{width:1200px;height:2655px;overflow:hidden;background:var(--white)}
body{position:relative;font-family:"Open Sans",Arial,sans-serif;color:var(--text)}

/* ---------- header ---------- */
.social-links{position:absolute;top:14px;left:872px;display:flex;gap:10px}
.social-links span{width:24px;height:24px;border-radius:50%;background:var(--ink);display:block}

.brand{position:absolute;top:52px;left:165px;font-family:"Arvo",Georgia,serif;font-weight:700;font-size:32px;color:var(--brand-blue);letter-spacing:-.5px}

.main-nav{position:absolute;top:53px;left:398px;width:636px;height:57px}
.main-nav svg{position:absolute;inset:0}
.main-nav ul{position:absolute;top:18px;left:70px;display:flex;gap:33px;list-style:none}
.main-nav a{font-family:"Arvo",Georgia,serif;font-weight:700;font-size:16px;color:var(--white);text-decoration:none}

/* ---------- hero ---------- */
.hero{position:absolute;top:110px;left:165px;width:869px;height:341px;background:var(--hero-bg);border-radius:0 0 8px 8px;overflow:hidden}
.hero-photo{position:absolute;left:0;top:0;width:370px;height:100%;background:linear-gradient(100deg,#c9b2a0 0%,#e7d3c4 45%,#2fb7cf 60%,#f3f3f3 75%)}
.hero-quote{position:absolute;left:378px;top:138px;font-family:"Arvo",Georgia,serif;font-size:26px;line-height:35px;color:#222}
.hero-dots{position:absolute;right:26px;bottom:22px;display:flex;gap:6px}
.hero-dots span{width:14px;height:14px;border-radius:50%;background:var(--white)}
.hero-dots span.active{background:var(--brand-blue)}

/* ---------- blog column ---------- */
.section-title{position:absolute;top:498px;left:165px;font-family:"Arvo",Georgia,serif;font-weight:700;font-size:22px;color:var(--brand-blue)}
.blog-posts{position:absolute;top:538px;left:165px;width:573px}
.post{height:496px}
.post-media{position:relative;height:212px;border:1px solid var(--line)}
.post-media .play{position:absolute;left:50%;top:50%;width:80px;height:80px;margin:-40px 0 0 -40px}
.media-apple{background:linear-gradient(90deg,#f2d9cc 0%,#c53a2c 25%,#e9c24a 38%,#f4e3da 60%,#faf6f3 100%)}
.media-salad{background:linear-gradient(90deg,#fafafa 0%,#5aa23a 15%,#a6cf7e 35%,#f1f1f1 55%,#fbfbfb 100%)}
.media-waist{background:linear-gradient(90deg,#7a9a6a 0%,#a9bf93 35%,#c38f78 60%,#e25683 75%,#c99f86 100%)}
.media-fruit{background:linear-gradient(90deg,#fdfdfd 0%,#e6902f 15%,#d8b060 30%,#c9362f 45%,#3c7d2e 60%,#e0d13a 80%,#fdfdfd 100%)}
.post h3{margin-top:18px;font-family:"Arvo",Georgia,serif;font-weight:700;font-size:15px;color:var(--ink)}
.post p{margin-top:6px;padding-left:8px;font-size:12.5px;line-height:22px;color:var(--text)}
.comments-label{display:flex;align-items:center;gap:8px;margin-top:20px;font-size:13px;font-weight:700;color:var(--ink)}
.comment-box{margin-top:12px;height:88px;background:var(--field-bg);border:1px solid var(--line);border-radius:6px;padding:10px 14px;font-size:12px;font-style:italic;color:var(--muted)}

/* ---------- sidebar ---------- */
.sidebar{position:absolute;top:513px;left:757px;width:277px}
.search{height:30px;border:2px solid var(--line);display:flex;align-items:center;justify-content:space-between;padding:0 8px;font-size:11px;color:var(--muted)}
.about{position:relative;height:211px;margin-top:14px}
.about-photo{position:absolute;left:57px;top:0;width:112px;height:211px;background:linear-gradient(180deg,#f5f5f5 0%,#e5c9b3 30%,#1c3f73 55%,#12305c 100%);border-radius:40px 40px 0 0}
.about-title{position:absolute;left:172px;top:36px;font-family:"Arvo",Georgia,serif;line-height:1}
.about-title .kicker{display:block;font-weight:700;font-size:18px;color:var(--brand-blue)}
.about-title .name{display:block;margin-top:4px;font-size:25px;color:#4a4a4a;white-space:nowrap}
.about-card{height:163px;background:var(--panel-dark);border-radius:0 0 6px 6px;padding:18px 14px;font-size:12.5px;line-height:22px;color:#e8e8e8}
.about-card strong{font-family:"Arvo",Georgia,serif;font-weight:400;font-size:19px;color:var(--brand-blue)}

.optin{margin-top:26px;height:503px;background:var(--brand-blue);border-radius:4px;padding:25px 15px 0}
.field{height:43px;background:var(--white);border-radius:5px;padding:0 10px;display:flex;align-items:center;font-size:12px;color:#444}
.optin h2{margin-top:16px;font-family:"Arvo",Georgia,serif;font-weight:700;font-size:42px;line-height:40px;color:var(--white)}
.optin h2 span{display:block;font-weight:400;font-size:28px;line-height:34px}
.optin p{margin:14px 0 22px;font-size:16px;line-height:26px;color:var(--white)}
.optin .field + .field{margin-top:9px}
.submit{display:block;margin:14px auto 0;width:134px;height:41px;background:var(--panel-dark);border-radius:4px;color:var(--white);font-family:"Arvo",Georgia,serif;font-weight:700;font-size:16px;text-align:center;line-height:41px}

.widget-title{margin-top:20px;font-family:"Arvo",Georgia,serif;font-weight:700;font-size:15px;color:var(--ink)}
.featured-video{position:relative;margin-top:12px;height:163px;border-radius:6px;background:linear-gradient(180deg,#cfe3b4 0%,#e8d4c4 40%,#f0f0f0 65%,#d9a93a 80%,#6ea83a 100%)}
.featured-video .play{position:absolute;left:50%;top:50%;width:54px;height:54px;margin:-27px 0 0 -27px}
.archives{margin-top:48px}
.archives ul{list-style:none;margin-top:22px}
.archives li{font-size:13px;line-height:27px;color:var(--ink)}

/* ---------- footer ---------- */
.site-footer{position:absolute;left:0;top:2496px;width:1200px;height:159px;background:var(--brand-blue);text-align:center;color:var(--white)}
.footer-nav{margin-top:18px;font-family:"Arvo",Georgia,serif;font-weight:700;font-size:16px}
.footer-nav span{margin:0 14px}
.disclaimer{width:870px;margin:10px auto 0;font-size:10.5px;line-height:15px}
.copyright{margin-top:22px;font-size:12px}
</style>
</head>
<body>

<header>
  <div class="social-links" aria-label="Social links">
    <span></span><span></span><span></span><span></span><span></span>
  </div>
  <div class="brand">brightpathYOU</div>
  <nav class="main-nav">
    <svg width="636" height="57" viewBox="0 0 636 57"><path d="M28 0H628a8 8 0 0 1 8 8V57H0Z" fill="#0d8ccc"/></svg>
    <ul>
      <li><a href="#">Home</a></li>
      <li><a href="#">About me</a></li>
      <li><a href="#">Blog</a></li>
      <li><a href="#">Recipes</a></li>
      <li><a href="#">Products</a></li>
      <li><a href="#">Contact us</a></li>
    </ul>
  </nav>
</header>

<section class="hero">
  <div class="hero-photo" role="img" aria-label="Photo of a slim woman measuring her waist"></div>
  <p class="hero-quote">“No hunger, no deprivation, no pills,<br>no weighing foods or calorie counting”</p>
  <div class="hero-dots"><span class="active"></span><span></span><span></span><span></span></div>
</section>

<h2 class="section-title">Blog Posts</h2>

<main class="blog-posts">
  <article class="post">
    <div class="post-media media-apple" role="img" aria-label="Video still: woman with an apple and measuring tape">
      <svg class="play" viewBox="0 0 80 80"><circle cx="40" cy="40" r="37" fill="#3a3a3a" stroke="#fff" stroke-width="4"/><path d="M32 25L57 40L32 55Z" fill="#fff"/></svg>
    </div>
    <h3>Lorem Ipsum is simply dummy text of the printing</h3>
    <p>Ever since the 1500s, when an unknown printer took a galley of type and scrambled it to make a type specimen book. It has survived not only five centuries, but also the leap into electronic typesetting, remaining essentially unchanged.</p>
    <div class="comments-label"><svg width="22" height="16" viewBox="0 0 22 16"><ellipse cx="8" cy="7" rx="8" ry="6" fill="#333"/><ellipse cx="15" cy="9" rx="7" ry="5.5" fill="#333"/><path d="M3 11L1 16L8 12Z" fill="#333"/></svg>Comments</div>
    <div class="comment-box">Type Your Comments ....</div>
  </article>

  <article class="post">
    <div class="post-media media-salad" role="img" aria-label="Video still: woman eating a bowl of salad">
      <svg class="play" viewBox="0 0 80 80"><circle cx="40" cy="40" r="37" fill="#3a3a3a" stroke="#fff" stroke-width="4"/><path d="M32 25L57 40L32 55Z" fill="#fff"/></svg>
    </div>
    <h3>Lorem Ipsum is simply dummy text of the printing</h3>
    <p>Ever since the 1500s, when an unknown printer took a galley of type and scrambled it to make a type specimen book. It has survived not only five centuries, but also the leap into electronic typesetting, remaining essentially unchanged.</p>
    <div class="comments-label"><svg width="22" height="16" viewBox="0 0 22 16"><ellipse cx="8" cy="7" rx="8" ry="6" fill="#333"/><ellipse cx="15" cy="9" rx="7" ry="5.5" fill="#333"/><path d="M3 11L1 16L8 12Z" fill="#333"/></svg>Comments</div>
    <div class="comment-box">Type Your Comments ....</div>
  </article>

  <article class="post">
    <div class="post-media media-waist" role="img" aria-label="Video still: measuring tape around a waist outdoors">
      <svg class="play" viewBox="0 0 80 80"><circle cx="40" cy="40" r="37" fill="#3a3a3a" stroke="#fff" stroke-width="4"/><path d="M32 25L57 40L32 55Z" fill="#fff"/></svg>
    </div>
    <h3>Lorem Ipsum is simply dummy text of the printing</h3>
    <p>Ever since the 1500s, when an unknown printer took a galley of type and scrambled it to make a type specimen book. It has survived not only five centuries, but also the leap into electronic typesetting, remaining essentially unchanged.</p>
    <div class="comments-label"><svg width="22" height="16" viewBox="0 0 22 16"><ellipse cx="8" cy="7" rx="8" ry="6" fill="#333"/><ellipse cx="15" cy="9" rx="7" ry="5.5" fill="#333"/><path d="M3 11L1 16L8 12Z" fill="#333"/></svg>Comments</div>
    <div class="comment-box">Type Your Comments ....</div>
  </article>

  <article class="post">
    <div class="post-media media-fruit" role="img" aria-label="Video still: pear, apple and lemon with measuring tape">
      <svg class="play" viewBox="0 0 80 80"><circle cx="40" cy="40" r="37" fill="#3a3a3a" stroke="#fff" stroke-width="4"/><path d="M32 25L57 40L32 55Z" fill="#fff"/></svg>
    </div>
    <h3>Lorem Ipsum is simply dummy text of the printing</h3>
    <p>Ever since the 1500s, when an unknown printer took a galley of type and scrambled it to make a type specimen book. It has survived not only five centuries, but also the leap into electronic typesetting, remaining essentially unchanged.</p>
    <div class="comments-label"><svg width="22" height="16" viewBox="0 0 22 16"><ellipse cx="8" cy="7" rx="8" ry="6" fill="#333"/><ellipse cx="15" cy="9" rx="7" ry="5.5" fill="#333"/><path d="M3 11L1 16L8 12Z" fill="#333"/></svg>Comments</div>
    <div class="comment-box">Type Your Comments ....</div>
  </article>
</main>

<aside class="sidebar">
  <div class="search">Search<svg width="10" height="10" viewBox="0 0 10 10"><circle cx="4" cy="4" r="3" fill="none" stroke="#aaa" stroke-width="1.4"/><path d="M6.3 6.3L9.5 9.5" stroke="#aaa" stroke-width="1.4"/></svg></div>

  <div class="about">
    <div class="about-photo" role="img" aria-label="Portrait of Ned Brook in a navy sweater"></div>
    <div class="about-title"><span class="kicker">About Me</span><span class="name">Ned Brook</span></div>
  </div>
  <div class="about-card"><strong>Ned Brook</strong> Lorem Ipsum is simply dummy text of the printing and typesetting industry. Lorem Ipsum has been the industry's standard dummy text ever since the 1500s, when an unknown</div>

  <form class="optin">
    <div class="field">Enter Name</div>
    <h2>Free<span>video &amp; eBook</span></h2>
    <p>Every Plate Tells A Story, Every Meal Builds A Habit-And How You Can Shape Yours Today</p>
    <div class="field">First Name</div>
    <div class="field">Last Name</div>
    <div class="field">E-Mail Address</div>
    <span class="submit">Submit</span>
  </form>

  <h3 class="widget-title">Featured Videos</h3>
  <div class="featured-video" role="img" aria-label="Video still: smiling woman behind a table of fresh fruit">
    <svg class="play" viewBox="0 0 80 80"><circle cx="40" cy="40" r="37" fill="#3a3a3a" stroke="#fff" stroke-width="4"/><path d="M32 25L57 40L32 55Z" fill="#fff"/></svg>
  </div>

  <div class="archives">
    <h3 class="widget-title">Archieves</h3>
    <ul>
      <li>2011 (12)</li>
      <li>2012 (12)</li>
      <li>2014 (12)</li>
    </ul>
  </div>
</aside>

<footer class="site-footer">
  <nav class="footer-nav">Home<span>|</span>About Me<span>|</span>Blog<span>|</span>Recipes<span>|</span>Products<span>|</span>Contact us</nav>
  <p class="disclaimer">“This website expresses the opinions of the author, is intended for informational and educational purposes only, should not be construed as medical or dietary advice, and is not intended to be a substitute for same. Before changing diets, medications, or before undertaking a weight loss regimen, be sure to consult with your physician. This information is not intended to diagnose or treat any illness or health problems you may be experiencing, so kindly address your doctor with these concerns.”</p>
  <p class="copyright">Copyright 2014, Ned Brook, All Rights Reserved</p>
</footer>

</body>
</html>
```